Twin Ravens Sparkling

Hi all,

Thanks for taking the time to check out our brief.

Twin Ravens is an Australian wine company based in Victoria, and have been around for more than 20 years. We have a well-known sparkling Chardonnay Pinot Noir that needs a package revamp and we need your help!

Check out our current package here: http://www.twinravens.example.au/our-wines/dsp-default_b.cfm?loadref=17

So here's the brief:

1. Use of the Twin Ravens logo (silhouette) and text mandatory - but can be as small/large as required.

2. Design must be shown on a sparkling bottle.

3. Can be closed with cork or crown seal - neck label/hood not mandatory.

4. Front label size to be no larger than 75mm high x 100mm wide. Back label to be no larger than 75mm x 100mm

5. Label does not have to be square/rectangular. Happy to see thoughts outside the box.

6. Design cannot be printed onto the bottle - must be on a label that can be applied to the bottle.

7. Be forward thinking. Be interesting. This design does not have to tie into our still (red and white) wine range.

8. Mandatory information to be shown on front label - a. Wine of Australia - b. Sparkling Chardonnay Pinot Noir

9. Mandatory info for front label - a. 750mL - b. Alcohol e.g. 13.5% ALC/VOL - c. Wine of Australi - d. Producer address (please insert dummy address at this stage - e. standard drinks e.g. approx 8.0 standard drinks (this can also be shown in the standard drinks glass logo) - f. space for a tasting blurb

10. Try to stay away from anything floral or overly girly.

Requirements
Must have
• Design must be shown on a sparkling wine bottle & include the full label design separately
Should not have
• Try to stay away from anything too floral and overly girly.

```html
<!DOCTYPE html>
<html lang="en">
<head>
<meta charset="utf-8">
<title>Twin Ravens Sparkling – Label Set</title>
<link rel="stylesheet" href="https://fonts.googleapis.com/css2?family=Cormorant+SC:wght@500&family=Roboto+Condensed:wght@400&display=swap">
<style>
  :root {
    --paper: #ffffff;
    --brown: #3a1a14;
    --brown-deep: #2a110c;
    --gold-light: #f2e37e;
    --gold-dark: #c7ae55;
    --gold-rich: #d9a92a;
    --gold-scroll: #e3c04e;
    --ink: #3a1a14;
    --cream: #f3ece2;
  }
  html, body {
    margin: 0;
    padding: 0;
    width: 1200px;
    height: 1000px;
    overflow: hidden;
    background: var(--paper);
  }
  .label-board { display: block; width: 1200px; height: 1000px; }
  .brand-serif {
    font-family: "Cormorant SC", "Times New Roman", serif;
    font-weight: 500;
    fill: var(--ink);
  }
  .info-sans {
    font-family: "Roboto Condensed", "Arial Narrow", sans-serif;
    fill: var(--ink);
  }
  .hood-text {
    font-family: "Roboto Condensed", "Arial Narrow", sans-serif;
    fill: var(--cream);
  }
</style>
</head>
<body>
<svg class="label-board" width="1200" height="1000" viewBox="0 0 1200 1000" xmlns="http://www.w3.org/2000/svg">
  <defs>
    <linearGradient id="goldSheet" x1="0" x2="1" y1="0" y2="0">
      <stop offset="0" stop-color="var(--gold-dark)"/>
      <stop offset="0.45" stop-color="var(--gold-light)"/>
      <stop offset="1" stop-color="var(--gold-dark)"/>
    </linearGradient>
    <linearGradient id="brownBand" x1="0" x2="0" y1="0" y2="1">
      <stop offset="0" stop-color="var(--brown-deep)"/>
      <stop offset="0.5" stop-color="#8a6a60"/>
      <stop offset="1" stop-color="var(--brown-deep)"/>
    </linearGradient>
    <radialGradient id="goldPanel" cx="0.5" cy="0.5" r="0.7">
      <stop offset="0" stop-color="#f8e88a"/>
      <stop offset="0.6" stop-color="var(--gold-rich)"/>
      <stop offset="1" stop-color="#b98a1c"/>
    </radialGradient>
    <radialGradient id="scrollTone" cx="0.5" cy="0.5" r="0.7">
      <stop offset="0.55" stop-color="#f0d877"/>
      <stop offset="1" stop-color="var(--gold-scroll)"/>
    </radialGradient>
  </defs>

  <!-- Back label -->
  <g class="back-label">
    <path d="M145 62 Q310 48 475 62 L475 462 Q310 448 145 462 Z" fill="url(#goldSheet)"/>
    <path d="M143 50 Q310 36 477 50 L477 66 Q310 52 143 66 Z" fill="url(#brownBand)"/>
    <path d="M143 456 Q310 442 477 456 L477 472 Q310 458 143 472 Z" fill="url(#brownBand)"/>
    <text class="brand-serif" x="312" y="112" font-size="30" text-anchor="middle" letter-spacing="3">TWIN RAVENS</text>
    <g class="address-box" fill="none" stroke="var(--ink)" stroke-width="1" stroke-dasharray="4 3">
      <rect x="218" y="353" width="172" height="72"/>
      <line x1="222" y1="385" x2="386" y2="385"/>
      <line x1="222" y1="400" x2="386" y2="400"/>
      <line x1="222" y1="413" x2="386" y2="413"/>
    </g>
    <text class="info-sans" x="304" y="370" font-size="11" text-anchor="middle">Producer Address</text>
  </g>

  <!-- Front label -->
  <g class="front-label">
    <path d="M137 533 Q303 519 470 533 L470 937 Q303 923 137 937 Z" fill="url(#goldSheet)"/>
    <path d="M137 522 Q303 508 470 522 L470 538 Q303 524 137 538 Z" fill="url(#brownBand)"/>
    <path d="M137 930 Q303 916 470 930 L470 946 Q303 932 137 946 Z" fill="url(#brownBand)"/>
    <rect class="scroll-frame" x="162" y="555" width="283" height="357" rx="40" fill="url(#scrollTone)" stroke="var(--brown)" stroke-width="4" role="img" aria-label="Gold scrollwork border ornament"/>
    <rect x="178" y="571" width="251" height="325" rx="28" fill="none" stroke="var(--brown)" stroke-width="2"/>
    <rect x="188" y="581" width="231" height="305" rx="20" fill="none" stroke="#b8901f" stroke-width="1.5"/>
    <path class="center-panel" d="M212 620 Q303 605 395 620 Q385 730 395 845 Q303 832 212 845 Q222 730 212 620 Z" fill="url(#goldPanel)" stroke="var(--brown)" stroke-width="2"/>
    <circle cx="232" cy="640" r="9" fill="#6a3a18" opacity="0.75" role="img" aria-label="Grape cluster ornament"/>
    <circle cx="374" cy="640" r="9" fill="#6a3a18" opacity="0.75" role="img" aria-label="Grape cluster ornament"/>
    <text class="brand-serif" x="303" y="690" font-size="24" text-anchor="middle" letter-spacing="2.5">TWIN RAVENS</text>
    <line x1="250" y1="702" x2="356" y2="702" stroke="var(--brown)" stroke-width="1"/>
    <rect x="284" y="716" width="38" height="40" rx="8" fill="#7a4a1a" opacity="0.55" role="img" aria-label="Grape and vine ornament"/>
    <text class="info-sans" x="303" y="790" font-size="15" text-anchor="middle">Wine of Australia</text>
    <text class="info-sans" x="303" y="808" font-size="10" text-anchor="middle">Sparkling Chardonnay Pinot Noir</text>
    <text class="info-sans" x="303" y="832" font-size="8.5" text-anchor="middle">750mL  Alcohol e.g. 13.5% ALC/VOL</text>
  </g>

  <!-- Neck hood -->
  <g class="neck-hood">
    <path d="M957 135 L1080 135 L1080 245 Q1080 300 1018 312 Q957 300 957 245 Z" fill="var(--brown-deep)"/>
    <rect x="948" y="76" width="140" height="60" rx="18" fill="var(--brown-deep)"/>
    <rect x="948" y="88" width="140" height="4" fill="#5a3a32"/>
    <text class="hood-text" x="1018" y="177" font-size="9.5" text-anchor="middle">Wine of Australia</text>
    <text class="hood-text" x="1018" y="190" font-size="9.5" text-anchor="middle">Sparkling Chardonnay Pinot Noir</text>
    <path d="M962 268 L1074 268 L1066 278 L1074 288 L962 288 L970 278 Z" fill="#bfb3ad"/>
    <text class="brand-serif" x="1018" y="283" font-size="11" text-anchor="middle" letter-spacing="1.5">TWIN RAVENS</text>
    <rect x="966" y="300" width="104" height="30" rx="10" fill="var(--brown-deep)" opacity="0.85" role="img" aria-label="Grape vine ornament"/>
  </g>
</svg>
</body>
</html>
```